Business Card Design Project

1. Show the company logo.
2. Only company email ID and website address to be shown (office@zolotoyveter.fm , www.zolotoyveter.fm).
3. Logo to be provided by us, 2 designs just in case. The logo is made with ' Zolotoy Veter' text, need to be edited so that it shows 'Tikhaya Gavan' instead .
4. Single sided business card, portrait or landscape is not a problem; back side to be filled with colors or a design that matches the logo the best.
5. Logo is to be embossed.
6. We're looking at an English and Russian version.
7. any other better idea is always welcomed.

```html
<!DOCTYPE html>
<html lang="en">
<head>
<meta charset="utf-8">
<title>Tikhaya Gavan — Business Card</title>
<link rel="stylesheet" href="https://fonts.googleapis.com/css2?family=Mulish:wght@400;700;800&display=swap">
<style>
  :root {
    --pattern-dark: #3a1f2e;
    --pattern-mid: #34506f;
    --pattern-light: #3f8fc6;
    --card-blue-light: #4b93de;
    --card-blue-mid: #3a7bc6;
    --card-blue-dark: #2c63a4;
    --emblem-navy: #0b3a74;
    --emblem-navy-deep: #072c5c;
    --brand-gold: #ffbf00;
    --text-white: #ffffff;
    --text-soft: #e4efff;
  }
  * { margin: 0; padding: 0; box-sizing: border-box; }
  html, body {
    width: 1050px;
    height: 1200px;
    overflow: hidden;
    background: var(--card-blue-dark);
  }
  .sheet {
    position: relative;
    width: 1050px;
    height: 1200px;
    font-family: "Mulish", "Century Gothic", sans-serif;
  }

  /* Back side */
  .card-back {
    position: absolute;
    left: 0; top: 0;
    width: 1050px; height: 602px;
    background:
      radial-gradient(circle at 50% 50%, var(--pattern-mid) 0%, var(--pattern-dark) 75%);
  }
  .card-back__pattern {
    position: absolute; inset: 0;
    background: linear-gradient(135deg, rgba(63,143,198,0.35), rgba(58,31,46,0.25) 50%, rgba(63,143,198,0.35));
  }
  .card-back__name {
    position: absolute;
    left: 0; right: 0; top: 262px;
    text-align: center;
    font-weight: 800;
    font-size: 58px;
    letter-spacing: 1px;
    color: var(--brand-gold);
  }

  /* Front side */
  .card-front {
    position: absolute;
    left: 0; top: 602px;
    width: 1050px; height: 598px;
    overflow: hidden;
    background: radial-gradient(circle at 560px 210px, var(--card-blue-light) 0%, var(--card-blue-mid) 45%, var(--card-blue-dark) 100%);
  }
  .card-front__rings {
    position: absolute; inset: 0;
  }
  .emblem {
    position: absolute;
    left: 42px; top: 156px;
    width: 340px; height: 340px;
    border-radius: 50%;
    background: radial-gradient(circle at 50% 30%, var(--emblem-navy) 0%, var(--emblem-navy-deep) 100%);
    box-shadow: 0 18px 40px rgba(10, 35, 80, 0.45);
    display: flex;
    align-items: center;
    justify-content: center;
  }
  .emblem__name {
    font-weight: 800;
    font-size: 38px;
    line-height: 1.1;
    text-align: center;
    color: var(--brand-gold);
  }
  .contact {
    position: absolute;
    left: 430px; top: 296px;
  }
  .contact__email {
    font-weight: 800;
    font-size: 26px;
    color: var(--text-white);
    line-height: 30px;
  }
  .contact__web {
    font-weight: 400;
    font-size: 19px;
    color: var(--text-soft);
    line-height: 26px;
  }
</style>
</head>
<body>
<main class="sheet">
  <section class="card-back">
    <div class="card-back__pattern" role="img" aria-label="Repeating geometric diamond ornament in blue on dark plum"></div>
    <div class="card-back__name">Tikhaya Gavan</div>
  </section>

  <section class="card-front">
    <svg class="card-front__rings" width="1050" height="598" viewBox="0 0 1050 598" aria-hidden="true">
      <circle cx="230" cy="380" r="320" fill="none" stroke="rgba(255,255,255,0.05)" stroke-width="70"/>
      <circle cx="230" cy="380" r="420" fill="none" stroke="rgba(255,255,255,0.04)" stroke-width="4"/>
    </svg>

    <div class="emblem">
      <div class="emblem__name">Tikhaya<br>Gavan</div>
    </div>

    <div class="contact">
      <p class="contact__email">office@zolotoyveter.fm</p>
      <p class="contact__web">www.zolotoyveter.fm</p>
    </div>
  </section>
</main>
</body>
</html>
```